Corvell Tarn manufacturing Project

We are looking at getting a brand new design for a new company that deals in selling stainless tubing and other stainless still products such as handrails, Spigots, Balustrade Fittings
Glass, Glass fittings and Aluminium Channels

We require a very clean website that deals with the following colours:

Blue to light blues
Blacks
Greys to light Greys
Whites

We are open for other ideas BUT we *DO NOT* want any pinks, greens or bright colours except for backgrounds colours we have chosen above. (It can be solid, gradient or a subtle pattern)

YOU MUST KEEP THE LOGO AS IS. PLEASE DO NOT ALTER THE LOGO IN *ANY WAY* and the logo MUST be the same colours and fonts.

Logo is attached.

The site must contain these aspects:
jQuery Slider (Image slide show)
Top drop down Menus
Be no more than 900px wide
Text is to be to the k9R standards. (no special fonts)

We will chop up the design into html format. You just need to provide the PSD file.

The clients opposition is:
www.polbrenwick.com

It Company

• Alter the logo in anyway

```html
<!DOCTYPE html>
<html lang="en">
<head>
<meta charset="utf-8">
<title>Corvell Tarn Metal</title>
<link rel="stylesheet" href="https://fonts.googleapis.com/css2?family=Arimo:ital,wght@0,400;0,700;1,400&family=PT+Sans:wght@400;700&display=swap">
<style>
:root{
  --backdrop-dark:#2c2c2c;
  --backdrop-mid:#4a4a4a;
  --panel:#ffffff;
  --footer-bg:#ececec;
  --rule:#cfcfcf;
  --ink:#333333;
  --ink-soft:#555555;
  --nav-ink:#555555;
  --brand-blue:#2e4a70;
  --button-top:#7fa6d3;
  --button-bottom:#3f6fa8;
  --overlay:rgba(96,112,128,0.78);
  --dot-dark:#0d1d5a;
  --box-bg:#f3f3f3;
}
*{margin:0;padding:0;box-sizing:border-box}
html,body{width:1200px;height:1134px;overflow:hidden}
body{
  position:relative;
  background:radial-gradient(circle at 50% 40%,var(--backdrop-mid),var(--backdrop-dark));
  font-family:"Arimo",Arial,sans-serif;color:var(--ink);
}
.page{position:absolute;left:178px;top:39px;width:844px;height:1050px;background:var(--panel);border-radius:8px;overflow:hidden}
.abs{position:absolute}

/* header */
.phone-tab{left:647px;top:0;width:197px;height:29px;background:linear-gradient(#f4f4f4,#e2e2e2);border-bottom-left-radius:28px;display:flex;align-items:center;padding-left:44px;gap:8px;color:#b8b8b8;font-weight:700;font-size:17px}
.brand-mark{left:38px;top:29px;width:67px;height:67px;border-radius:50%;background:#2f4e78}
.brand-name{left:116px;top:50px;font-size:18px;color:#222}
.brand-sub{left:129px;top:74px;font-size:8.5px;letter-spacing:1.6px;color:#222}
.nav{left:0;top:48px;width:844px;height:30px}
.nav a{position:absolute;top:0;height:30px;line-height:30px;font-size:11.5px;font-weight:700;color:var(--nav-ink);text-decoration:none}
.nav .current{left:291px;width:84px;text-align:center;color:#fff;border-radius:10px;background:linear-gradient(var(--button-top),var(--button-bottom));box-shadow:0 0 0 3px #e4e4e4,0 1px 2px rgba(0,0,0,.4)}

/* slider */
.slider{left:0;top:118px;width:844px;height:315px;background:linear-gradient(120deg,#c9d2d8 0%,#9aa4ab 45%,#e8eef1 75%,#f6f8f9 100%)}
.slider-overlay{left:0;top:0;width:429px;height:315px;background:var(--overlay)}
.slide-title{left:38px;top:62px;font-family:"PT Sans",sans-serif;font-weight:700;font-size:31px;color:#fff}
.slide-text{left:37px;top:112px;width:360px;font-family:"PT Sans",sans-serif;font-size:22px;line-height:28px;color:#fff}
.slide-button{left:38px;top:192px;width:240px;height:46px;border-radius:4px;background:linear-gradient(var(--button-top),var(--button-bottom));color:#fff;font-family:"PT Sans",sans-serif;font-weight:700;font-size:19px;letter-spacing:.5px;display:flex;align-items:center;justify-content:center;gap:12px}
.dots{left:734px;top:281px;display:flex;gap:7px}
.dots span{width:13px;height:13px;border-radius:50%;background:var(--dot-dark)}
.dots span:first-child{background:#fff}

/* product tiles */
.tile{top:461px;width:233px;height:149px;border-radius:7px;overflow:hidden;box-shadow:0 0 0 2px #e6e6e6}
.tile-caption{position:absolute;left:0;bottom:0;width:100%;height:46px;background:rgba(90,90,90,.8);color:#fff;font-family:"PT Sans",sans-serif;font-size:19px;line-height:46px;text-align:center}

/* intro */
.intro-title{left:37px;top:634px;font-size:24px;font-weight:700;color:var(--brand-blue)}
.intro-text{left:37px;top:672px;width:510px;font-size:12.5px;line-height:18.75px}
.advantages{left:572px;top:638px;width:234px;height:126px;background:var(--box-bg);border-radius:8px;padding:12px 0 0 29px}
.advantages h3{font-size:14.5px;font-weight:700;color:var(--brand-blue);margin-bottom:5px}
.advantages li{list-style:none;display:flex;align-items:center;gap:13px;font-size:12.5px;font-style:italic;color:#555;height:18.75px}

/* footer */
.footer{left:0;top:793px;width:844px;height:257px;background:var(--footer-bg);border-top:2px solid var(--rule)}
.footer h4{position:absolute;top:22px;font-size:14px;font-weight:700;color:var(--ink-soft)}
.footer-links{left:37px;top:60px;font-size:11.5px;line-height:18.75px;color:#444;list-style:none}
.testimonial{left:213px;top:60px;width:300px;font-size:11.5px;line-height:18.75px;color:#444}
.testimonial strong{color:#111}
.product-thumb{left:537px;top:60px;width:84px;height:84px;background:linear-gradient(135deg,#5e6a6c,#cdd8d8 50%,#7a8a8c);border:1px solid #bbb}
.product-name{left:636px;top:61px;font-size:13.5px;font-weight:700;color:var(--brand-blue)}
.product-text{left:636px;top:84px;width:170px;font-size:11.5px;line-height:17.5px;color:#444}
.product-text a{color:var(--brand-blue)}
.footer-rule{left:0;top:198px;width:844px;height:1px;background:var(--rule)}
.copyright{left:37px;top:221px;font-size:11.5px;color:#444}
.social{left:736px;top:218px;display:flex;gap:14px}
.social span{width:16px;height:16px;border-radius:2px;background:#6f93bf}
</style>
</head>
<body>
<div class="page">
  <header>
    <div class="abs phone-tab">
      <svg width="16" height="16" viewBox="0 0 24 24" aria-hidden="true"><path fill="#bdbdbd" d="M6.6 10.8a15 15 0 0 0 6.6 6.6l2.2-2.2c.3-.3.7-.4 1-.2 1.1.4 2.3.6 3.6.6.6 0 1 .4 1 1V20c0 .6-.4 1-1 1A17 17 0 0 1 3 4c0-.6.4-1 1-1h3.5c.6 0 1 .4 1 1 0 1.3.2 2.5.6 3.6.1.3 0 .7-.2 1z"/></svg>
      123-456-7890
    </div>
    <div class="abs brand-mark"></div>
    <div class="abs brand-name">Corvell Tarn Metal</div>
    <div class="abs brand-sub">Manufacturing Co. Ltd</div>
    <nav class="abs nav">
      <a class="current" href="#">HOME</a>
      <a style="left:399px" href="#">ABOUT</a>
      <a style="left:489px" href="#">PRODUCTS</a>
      <a style="left:603px" href="#">TESTIMONIALS</a>
      <a style="left:733px" href="#">CONTACT</a>
    </nav>
  </header>

  <section class="abs slider" role="img" aria-label="Stainless steel handrail bracket fixed to a glass panel">
    <div class="abs slider-overlay"></div>
    <div class="abs slide-title">HANDRAILS</div>
    <div class="abs slide-text">High quality stainless handrails with various styles</div>
    <div class="abs slide-button">LEARN MORE
      <svg width="20" height="14" viewBox="0 0 20 14" aria-hidden="true"><path fill="#fff" d="M0 4h11V0l9 7-9 7v-4H0z"/></svg>
    </div>
    <div class="abs dots"><span></span><span></span><span></span><span></span></div>
  </section>

  <div class="abs tile" style="left:37px;background:linear-gradient(135deg,#8b8f94,#d5d8db 55%,#6e7378)" role="img" aria-label="Perforated stainless balustrade panel">
    <div class="tile-caption">Balustrade</div>
  </div>
  <div class="abs tile" style="left:303px;background:linear-gradient(135deg,#7c8687,#d7dfe0 50%,#5a6466)" role="img" aria-label="Glass panels held by steel fittings">
    <div class="tile-caption">Glass Fittings</div>
  </div>
  <div class="abs tile" style="left:572px;background:linear-gradient(135deg,#f4f4f4,#b9bcbf 55%,#e9eaeb)" role="img" aria-label="Chrome spigot with cross handles">
    <div class="tile-caption">Spigot</div>
  </div>

  <h1 class="abs intro-title">Corvell Tarn Metal</h1>
  <p class="abs intro-text">Lorem ipsum dolor sit amet, consectetur adipiscing elit. Etiam tristique tristique lacus in varius. Donec nec vestibulum ligula. Aenean turpis diam, feugiat a luctus in, rhoncus eget risus. Maecenas consequat porttitor dui, vitae consequat massa imperdiet ut. elit ut tempus lobortis, eros leo molestie velit, non egestas augue nulla eget erat.</p>

  <aside class="abs advantages">
    <h3>ADVANTAGES</h3>
    <ul>
      <li><svg width="15" height="14" viewBox="0 0 15 14" aria-hidden="true"><rect x="1" y="3" width="10" height="10" fill="none" stroke="#222" stroke-width="1.5"/><path d="M3 7l3 3 8-9" fill="none" stroke="#111" stroke-width="2.2"/></svg>Customized style</li>
      <li><svg width="15" height="14" viewBox="0 0 15 14" aria-hidden="true"><rect x="1" y="3" width="10" height="10" fill="none" stroke="#222" stroke-width="1.5"/><path d="M3 7l3 3 8-9" fill="none" stroke="#111" stroke-width="2.2"/></svg>1 year guarantee</li>
      <li><svg width="15" height="14" viewBox="0 0 15 14" aria-hidden="true"><rect x="1" y="3" width="10" height="10" fill="none" stroke="#222" stroke-width="1.5"/><path d="M3 7l3 3 8-9" fill="none" stroke="#111" stroke-width="2.2"/></svg>High quality</li>
      <li><svg width="15" height="14" viewBox="0 0 15 14" aria-hidden="true"><rect x="1" y="3" width="10" height="10" fill="none" stroke="#222" stroke-width="1.5"/><path d="M3 7l3 3 8-9" fill="none" stroke="#111" stroke-width="2.2"/></svg>Strong</li>
    </ul>
  </aside>

  <footer class="abs footer">
    <h4 style="left:37px">Browse Site</h4>
    <ul class="abs footer-links">
      <li>Home</li><li>About our company</li><li>Our Products</li><li>Our Prices</li><li>Client Testimonials</li><li>Contact us</li>
    </ul>
    <h4 style="left:213px">Client Testimonials</h4>
    <p class="abs testimonial">Lorem ipsum dolor sit amet, consectetur adipiscing elit. Etiam tristique tristique lacus in varius. Donec nec vestibulum ligula. Aenean turpis diam, feugiat a luctus in, rhoncus eget risus. Maecenas consequat porttitor dui, vitae consequat massa imperdiet ut. elit ut tempus .<br><strong>Dara, Owner Tarnwell Steel Company</strong></p>
    <h4 style="left:541px">Our Products</h4>
    <div class="abs product-thumb" role="img" aria-label="Glass fitting detail"></div>
    <div class="abs product-name">Glass Fittings</div>
    <p class="abs product-text">adipiscing elit. Etiam tristique tristique lacus in varius. Donec nec vestibulum ligula.<br><a href="#">read more</a></p>
    <div class="abs footer-rule"></div>
    <p class="abs copyright">Copyright © 2013 Corvell Tarn Metal. All rights reserved.</p>
    <div class="abs social" aria-label="Social links"><span></span><span></span><span></span></div>
  </footer>
</div>
</body>
</html>
```